Kettle Ledger Business Card design

We need a stand out business card design for Accounting practice based in Australia specialising in pubs, clubs and hotels. We help venues maximise margins, create time and manage cashflow. One club we have been working with for the last 6 months has increased revenue by 3% and margin by 5% in this time frame. We have a back office outsourced system that costs less than having a full time employee and also allows the venues the added benefit of:<br/>-using the office space to become a revenue generating opportunity. <br/>-a complete system to enhance governance, accountability and efficiency within their operation<br/>-52 weeks cover so no hassle to cover annual/sick .. leave<br/><br/>We would like to see designs that use the colours of our logo (green & blue).
Target Market(s)
Australian Pubs, Clubs & Hotels abookkeeping, accounting and tax services
Industry/Entity Type
Accountant
Contact Information for Business Card
Miriam Oakley CPA
Principal
Accountant Tax Agent
Miriam@KettleLedger-example.com.au
0418693142
www.kettleledger-example.com.au
Accounting / Payroll / Tax / SMSF / Technology
Colors
Designer to choose colors to be used in the design.
Look and feel
Each slider illustrates characteristics of the customer's brand and the style your logo design should communicate.

```html
<!DOCTYPE html>
<html lang="en">
<head>
<meta charset="utf-8">
<title>Kettle Ledger Business Card</title>
<link rel="stylesheet" href="https://fonts.googleapis.com/css2?family=Montserrat:wght@800&family=Open+Sans:wght@400;600&display=swap">
<style>
  :root {
    --brand-blue: #24408e;
    --brand-green: #1f7a3a;
    --ink: #222;
    --paper: #ffffff;
    --backdrop: #e9eaec;
  }
  * { margin: 0; padding: 0; box-sizing: border-box; }
  html, body { width: 1200px; height: 936px; overflow: hidden; }
  body {
    background: var(--backdrop);
    position: relative;
    font-family: "Open Sans", sans-serif;
  }
  .card {
    position: absolute;
    width: 560px;
    height: 342px;
    box-shadow: 0 6px 18px rgba(0,0,0,.18);
  }
  .card--front {
    left: 80px; top: 100px;
    background: var(--brand-blue);
    display: flex; align-items: center; justify-content: center;
  }
  .card--back {
    left: 560px; top: 494px;
    background: var(--paper);
    display: flex; align-items: center;
    padding-left: 48px;
  }
  .brand {
    display: flex; align-items: center; gap: 16px;
    font-family: "Montserrat", sans-serif;
    font-weight: 800;
    line-height: 1;
  }
  .brand__dot { border-radius: 50%; flex: none; }
  .card--front .brand { color: var(--paper); font-size: 48px; }
  .card--front .brand__dot { width: 70px; height: 70px; border: 5px solid var(--paper); }
  .card--back .brand { color: var(--brand-blue); font-size: 27px; gap: 12px; }
  .card--back .brand__dot { width: 44px; height: 44px; border: 4px solid var(--brand-green); }
  .divider {
    width: 2px; height: 104px;
    background: var(--brand-blue);
    margin: 0 22px 0 24px;
  }
  .contact__name {
    color: var(--brand-blue);
    font-weight: 600;
    font-size: 19px;
  }
  .contact__role {
    color: var(--ink);
    font-size: 13px;
    line-height: 1.3;
    margin-bottom: 10px;
  }
  .contact__list { list-style: none; }
  .contact__item {
    display: flex; align-items: center; gap: 6px;
    font-size: 12.5px; color: var(--ink);
    line-height: 1.55;
  }
  .contact__icon { width: 12px; height: 12px; fill: var(--brand-blue); flex: none; }
</style>
</head>
<body>
  <section class="card card--front">
    <div class="brand"><span class="brand__dot"></span>Kettle Ledger</div>
  </section>

  <section class="card card--back">
    <div class="brand"><span class="brand__dot"></span>Kettle Ledger</div>
    <div class="divider"></div>
    <div class="contact">
      <p class="contact__name">Miriam Oakley CPA</p>
      <p class="contact__role">Principal<br>Accountant Tax Agent</p>
      <ul class="contact__list">
        <li class="contact__item">
          <svg class="contact__icon" viewBox="0 0 24 24"><path d="M6.6 10.8a15.1 15.1 0 0 0 6.6 6.6l2.2-2.2a1 1 0 0 1 1-.25 11.4 11.4 0 0 0 3.6.57 1 1 0 0 1 1 1V20a1 1 0 0 1-1 1A17 17 0 0 1 3 4a1 1 0 0 1 1-1h3.5a1 1 0 0 1 1 1c0 1.25.2 2.45.57 3.57a1 1 0 0 1-.25 1z"/></svg>
          0418693142
        </li>
        <li class="contact__item">
          <svg class="contact__icon" viewBox="0 0 24 24"><path d="M2 5h20v14H2zm2 2v.5l8 5 8-5V7zm0 2.8V17h16V9.8l-8 5z"/></svg>
          Miriam@KettleLedger-example.com.au
        </li>
        <li class="contact__item">
          <svg class="contact__icon" viewBox="0 0 24 24"><circle cx="12" cy="12" r="10"/></svg>
          www.kettleledger-example.com.au
        </li>
      </ul>
    </div>
  </section>
</body>
</html>
```